Exciting letterhead design for startup company

We need a A4 letterhead designing.

See attached file which contains the logo (on 3 different coloured backgrounds) and then the address and contact information. It also contains 4 colours that can be used.

Looking for an imaginative design. We are a young, fresh startup website design company so need a letterhead that reflects our industry.

Font styles to use
Sans Serif

```html
<!DOCTYPE html>
<html lang="en">
<head>
<meta charset="utf-8">
<title>Brightloom Letterhead</title>
<link rel="stylesheet" href="https://fonts.googleapis.com/css2?family=Questrial&display=swap">
<style>
  :root {
    --backdrop: #c9cdd1;
    --paper: #f1f1f1;
    --ink: #3a3d42;
    --ink-soft: #4d5157;
    --brand-blue: #3a8fcf;
    --band-grey: #cfd1d3;
    --band-dark: #33363b;
    --rule: #b9bcbf;
  }
  html, body {
    margin: 0;
    padding: 0;
    width: 1200px;
    height: 1000px;
    overflow: hidden;
    background: var(--backdrop);
    font-family: "Questrial", "Century Gothic", sans-serif;
    color: var(--ink);
  }
  .sheet {
    position: absolute;
    left: 289px;
    top: 63px;
    width: 624px;
    height: 879px;
    background: var(--paper);
    overflow: hidden;
  }
  .brand-name {
    position: absolute;
    left: 58px;
    top: 46px;
    font-size: 38px;
    letter-spacing: -1.5px;
    color: var(--ink);
    line-height: 1;
  }
  .sender-address {
    position: absolute;
    right: 197px;
    top: 56px;
    text-align: right;
    font-size: 8.6px;
    line-height: 12.6px;
    font-style: normal;
    color: var(--ink-soft);
  }
  .header-divider {
    position: absolute;
    left: 441px;
    top: 58px;
    width: 1px;
    height: 38px;
    background: var(--rule);
  }
  .contact-list {
    position: absolute;
    left: 455px;
    top: 56px;
    margin: 0;
    padding: 0;
    list-style: none;
    font-size: 8.6px;
    color: var(--ink-soft);
  }
  .contact-list li {
    display: flex;
    align-items: center;
    height: 12.6px;
  }
  .contact-icon {
    width: 9px;
    height: 9px;
    margin-right: 6px;
    flex: none;
  }
  .letter-date, .recipient {
    position: absolute;
    left: 59px;
    font-size: 9.4px;
    line-height: 11.4px;
    color: var(--ink-soft);
  }
  .letter-date { top: 146px; }
  .recipient { top: 169px; }
  .fold-mark {
    position: absolute;
    left: 0;
    width: 29px;
    height: 1px;
    background: var(--rule);
  }
  .fold-mark.upper { top: 313px; }
  .fold-mark.lower { top: 624px; }
  .salutation {
    position: absolute;
    left: 59px;
    top: 294px;
    font-size: 9.4px;
    font-weight: bold;
    margin: 0;
  }
  .letter-body {
    position: absolute;
    left: 59px;
    top: 317px;
    width: 505px;
    font-size: 9.4px;
    letter-spacing: 0.12px;
    line-height: 11.4px;
    text-align: justify;
    color: var(--ink-soft);
  }
  .letter-body p { margin: 0 0 11.4px; }
  .closing {
    position: absolute;
    left: 59px;
    top: 565px;
    font-size: 9.2px;
    line-height: 11.6px;
    color: var(--ink-soft);
  }
  .closing strong { color: var(--ink); }
  .signature {
    position: absolute;
    left: 133px;
    top: 556px;
    width: 130px;
    height: 62px;
    background: linear-gradient(135deg, rgba(90,110,190,0.10), rgba(90,110,190,0.22));
    border-radius: 4px;
  }
  .footer-band {
    position: absolute;
    left: 0;
    bottom: 0;
    width: 624px;
    height: 46px;
    background: linear-gradient(180deg, var(--brand-blue) 0%, var(--band-grey) 45%, var(--band-dark) 100%);
  }
</style>
</head>
<body>
  <main class="sheet">
    <div class="brand-name">Brightloom</div>

    <address class="sender-address">
      Unit 4, Harbour Court<br>
      Weaver Lane, Leeds<br>
      LS2 7QP, United Kingdom
    </address>
    <div class="header-divider"></div>
    <ul class="contact-list">
      <li>
        <svg class="contact-icon" viewBox="0 0 10 10"><rect width="10" height="10" rx="2" fill="#3a8fcf"/><path d="M3 2.3 L4.2 3.6 L3.6 4.3 Q4.4 5.7 5.7 6.4 L6.4 5.8 L7.7 7 L7 7.8 Q4.5 7.6 2.3 3 Z" fill="#fff"/></svg>
        0845 210 7731
      </li>
      <li>
        <svg class="contact-icon" viewBox="0 0 10 10"><rect width="10" height="10" rx="2" fill="#3a8fcf"/><rect x="2" y="3" width="6" height="4.2" fill="none" stroke="#fff" stroke-width="0.8"/><path d="M2 3 L5 5.4 L8 3" fill="none" stroke="#fff" stroke-width="0.8"/></svg>
        hello@brightloom.co.uk
      </li>
      <li>
        <svg class="contact-icon" viewBox="0 0 10 10"><rect width="10" height="10" rx="2" fill="#3a8fcf"/><circle cx="5" cy="5" r="2.8" fill="none" stroke="#fff" stroke-width="0.8"/><circle cx="5" cy="5" r="1" fill="#fff"/></svg>
        @brightloom
      </li>
    </ul>

    <div class="letter-date">30.02.2015</div>
    <div class="recipient">
      Recipient's name<br>
      Lindenweg 12<br>
      10115 Berlin<br>
      Germany
    </div>

    <div class="fold-mark upper"></div>
    <div class="fold-mark lower"></div>

    <p class="salutation">Dear sir,</p>
    <div class="letter-body">
      <p>Communication is a very integral part of living creatures, animals and humans. Communication may be verbal or written. Written communication however is only applicable to human beings. Can you even imagine a world without communication? Verbal communication can be through telephones, webcams or in person. Written communication is through letters, emails and mobile phone messages.</p>
      <p>In today's world of great inventions and technology, letters have somehow become redundant. It is the time for text messages or chats. But they still can communicate a lot more than all other modes of communication. Organizations and various government departments still bank on letters as a strong medium of communication. There is no comparison in costs of sending letters as compared to costs of mobile phone messages though – letters are far cheaper. Letters now commonly known as "hard copy documents" are considered more relevant and important than email copies of text messages as proof or evidence of some sort.</p>
      <p>Letters speak volumes about a person or an organization that writes it. So one must take utmost care ensuring that the language used in any letter is appropriate for the occasion for which it is being written. Since a letter is also a written proof or document, if there are certain things that should not form a part of it, then that too should be carefully handled.</p>
      <p>Writing a good letter is an art. But if for some reason someone is unable to write that perfect letter, these different types of letters provide a base for you to build on. Sample letters have been given for everyone to understand what all information needs to form a part of the letter type and then it can be customized.</p>
    </div>

    <div class="closing">
      Yours Sincerely,<br>
      <strong>Elin Maroway</strong>
    </div>
    <div class="signature" role="img" aria-label="Handwritten signature of the sender"></div>

    <div class="footer-band" role="img" aria-label="Decorative footer band in brand blue, light grey and charcoal"></div>
  </main>
</body>
</html>
```